Redesign of PTO Calendar website

Looking to drastically improve our PTO (paid time off) Calendar look and feel. Need a modern and well thought out design that is fun.
Current Screenshots
https://files.brinvola.net/sheet/d/7vRt2mWq9LpZa4XkeN8sBy3dHcJ0fUoT6iQgEwMnY/view?mode=sharing
It's written in PHP and Laravel, if that matters. I am not necessarily attached to any of the current design, so please go wild. Current functionality needs to remain the same, but some can be added if you feel it would be of value. Layout can certainly change.
NOTE - this calendar can be used by any company, not just our own. So we'd like it to have a look and feel that is easy to navigate.
Site logo is attached.
Pages needed:
* Login Page
* Registration Page
* Calendar page
* Add PTO method
* Admin page (will use template for all admin areas)
* User profile page
Thanks!

```html
<!DOCTYPE html>
<html lang="en">
<head>
<meta charset="utf-8">
<title>Leavely – Teams</title>
<link href="https://fonts.googleapis.com/css2?family=Poppins:wght@400;500;600;700&display=swap" rel="stylesheet">
<style>
:root{
  --sidebar:#3d4a5c;
  --sidebar-icon:#4d5a6c;
  --brand:#0a78c8;
  --page:#f9f9f9;
  --white:#ffffff;
  --text:#3a4250;
  --muted:#6b7280;
  --row-alt:#f6f7f9;
  --active:#6fd47f;
  --danger:#f05a5a;
  --dash:#6d7888;
  --next:#36475a;
}
*{box-sizing:border-box;margin:0;padding:0}
html,body{width:1200px;height:844px;overflow:hidden}
body{font-family:"Poppins",sans-serif;background:var(--page);position:relative;color:var(--text)}
.sidebar{position:absolute;left:0;top:0;width:249px;height:844px;background:var(--sidebar);color:var(--white)}
.brand{position:absolute;left:51px;top:38px;display:flex;align-items:center;gap:8px;font-weight:700;font-size:28px;color:var(--white)}
.brand-dot{width:22px;height:22px;border-radius:50%;background:var(--brand)}
.nav-title{position:absolute;left:51px;top:128px;font-size:17px;font-weight:700;letter-spacing:.3px}
.nav-item{position:absolute;left:52px;display:flex;align-items:center;gap:11px;font-size:16px;font-weight:500}
.nav-icon{width:50px;height:50px;border-radius:50%;background:var(--sidebar-icon);display:flex;align-items:center;justify-content:center}
.nav-item.active .nav-icon{background:var(--brand)}
.nav-divider{position:absolute;left:111px;width:93px;border-top:1px dashed var(--dash)}
.user{position:absolute;left:948px;top:32px;display:flex;align-items:center;gap:12px;font-size:18px;font-weight:500;color:var(--text)}
.avatar{width:54px;height:54px;border-radius:50%;border:5px solid var(--white);box-shadow:0 3px 10px rgba(0,0,0,.1);background:radial-gradient(circle at 50% 45%,#c9956f 0 35%,#3f8e3a 36%)}
.toolbar-label{position:absolute;top:141px;font-size:14px;font-weight:500;color:var(--text);letter-spacing:.3px}
.search{position:absolute;left:357px;top:128px;width:215px;height:44px;background:var(--white);box-shadow:0 4px 14px rgba(0,0,0,.07);display:flex;align-items:center;justify-content:space-between;padding:0 16px 0 17px;font-size:15px;color:var(--muted)}
.select{position:absolute;left:982px;top:131px;width:88px;height:41px;border:1.5px solid #cfd4da;border-radius:5px;display:flex;align-items:center;justify-content:space-between;padding:0 11px 0 18px;font-size:17px;color:var(--text)}
.table-card{position:absolute;left:292px;top:204px;width:855px;height:427px;background:var(--white);border-radius:8px;box-shadow:0 4px 16px rgba(0,0,0,.08);overflow:hidden}
.table-head{height:48px;background:var(--brand);color:var(--white);font-size:15px;font-weight:600;position:relative}
.table-head span,.row span,.row svg{position:absolute}
.table-head span{top:13px}
.row{position:absolute;left:15px;width:825px;height:68px;border-radius:8px;font-size:14.5px;color:var(--muted)}
.row.alt{background:var(--row-alt)}
.row .name{left:22px;top:23px}
.row .sup{left:142px;top:23px}
.row .desc{left:263px;top:10px;line-height:20px;font-size:14.5px}
.row .count{left:540px;top:22px;font-size:16px}
.row .badge{left:638px;top:22px;width:71px;height:25px;border-radius:13px;background:var(--active);color:var(--white);font-size:12px;display:flex;align-items:center;justify-content:center}
.row .edit{left:748px;top:25px}
.row .trash{left:790px;top:24px}
.summary{position:absolute;left:291px;top:685px;font-size:18px;color:var(--text)}
.pager-btn{position:absolute;top:684px;height:31px;border-radius:3px;display:flex;align-items:center;justify-content:center;gap:6px;font-size:13px}
.prev{left:831px;width:78px;background:#e6e7e9;color:var(--muted)}
.next{left:1067px;width:78px;background:var(--next);color:var(--white);font-weight:500}
.page-num{position:absolute;top:691px;font-size:13px}
.page-current{position:absolute;left:946px;top:683px;width:34px;height:34px;border-radius:50%;background:var(--brand);color:var(--white);display:flex;align-items:center;justify-content:center;font-size:13px;font-weight:500}
.scrollbar{position:absolute;left:1171px;top:386px;width:5px;height:100px;border-radius:3px;background:#dcdcdc}
</style>
</head>
<body>
<aside class="sidebar">
  <div class="brand"><span>Leavely</span><span class="brand-dot"></span></div>
  <div class="nav-title">GENERAL</div>

  <div class="nav-item active" style="top:173px">
    <span class="nav-icon"><svg width="26" height="26" viewBox="0 0 24 24" fill="#fff"><circle cx="12" cy="5" r="2.5"/><circle cx="4.5" cy="17" r="2.5"/><circle cx="19.5" cy="17" r="2.5"/><path d="M9 9h6v3H9zM2 21h5v2H2zM17 21h5v2h-5z"/><path d="M8 12l-2 3M16 12l2 3M8 19h8" stroke="#fff" stroke-width="1.6" fill="none"/></svg></span>
    <span>Teams</span>
  </div>
  <div class="nav-divider" style="top:237px"></div>

  <div class="nav-item" style="top:249px">
    <span class="nav-icon"><svg width="22" height="22" viewBox="0 0 24 24" fill="#fff"><circle cx="12" cy="7" r="4"/><path d="M4 21c0-5 4-7 8-7s8 2 8 7z"/></svg></span>
    <span>Members</span>
  </div>
  <div class="nav-divider" style="top:309px"></div>

  <div class="nav-item" style="top:323px">
    <span class="nav-icon"><svg width="24" height="24" viewBox="0 0 24 24" fill="none" stroke="#fff" stroke-width="2"><rect x="3" y="4" width="18" height="12" rx="1"/><path d="M3 10h18M8 16v4l4-2 4 2v-4"/></svg></span>
    <span>PTO Types</span>
  </div>
  <div class="nav-divider" style="top:388px"></div>

  <div class="nav-item" style="top:406px">
    <span class="nav-icon"><svg width="24" height="24" viewBox="0 0 24 24" fill="none" stroke="#fff" stroke-width="1.8"><rect x="3" y="5" width="18" height="16" rx="2"/><path d="M3 9h18M8 3v4M16 3v4"/><path d="M7 13h2M11 13h2M15 13h2M7 17h2M11 17h2M15 17h2" stroke-width="1.6"/></svg></span>
    <span>Add PTO</span>
  </div>
</aside>

<div class="user">
  <div class="avatar" role="img" aria-label="User profile photo"></div>
  <span>Marcus Keller</span>
  <svg width="12" height="8" viewBox="0 0 12 8" fill="none" stroke="#3a4250" stroke-width="1.8"><path d="M1 1l5 5 5-5"/></svg>
</div>

<span class="toolbar-label" style="left:292px">SEARCH</span>
<div class="search"><span>Search</span>
  <svg width="18" height="18" viewBox="0 0 24 24" fill="none" stroke="#0a78c8" stroke-width="2.5"><circle cx="10" cy="10" r="7"/><path d="M15.5 15.5L21 21"/></svg>
</div>
<span class="toolbar-label" style="left:914px">SHOW</span>
<div class="select"><span>20</span>
  <svg width="12" height="8" viewBox="0 0 12 8" fill="none" stroke="#3a4250" stroke-width="1.8"><path d="M1 1l5 5 5-5"/></svg>
</div>
<span class="toolbar-label" style="left:1092px">ENTRIES</span>

<section class="table-card">
  <div class="table-head">
    <span style="left:34px">Team Name</span>
    <span style="left:153px">Supervisor</span>
    <span style="left:280px">Team Desc</span>
    <span style="left:506px">Resource Count</span>
    <span style="left:664px">Status</span>
  </div>

  <div class="row" style="top:51px">
    <span class="name">Nursing</span><span class="sup">Lena Farrow</span>
    <span class="desc">Lorem Ipsum is simply dummy<br>printing and typesetting...</span>
    <span class="count">0</span><span class="badge">ACTIVE</span>
    <svg class="edit" width="18" height="18" viewBox="0 0 24 24" fill="none" stroke="#0a78c8" stroke-width="2.2"><path d="M20 13v7H4V4h7"/><path d="M18 3l3 3-9 9H9v-3z"/></svg>
    <svg class="trash" width="16" height="19" viewBox="0 0 20 24" fill="#f05a5a"><path d="M1 4h18v2H1zM7 1h6v3H7zM3 7h14l-1 16H4zM7 9v12h1.5V9zM11.5 9v12H13V9z" fill-rule="evenodd"/></svg>
  </div>
  <div class="row alt" style="top:120px">
    <span class="name">Nursing</span><span class="sup">Lena Farrow</span>
    <span class="desc">Lorem Ipsum is simply dummy<br>printing and typesetting...</span>
    <span class="count">0</span><span class="badge">ACTIVE</span>
    <svg class="edit" width="18" height="18" viewBox="0 0 24 24" fill="none" stroke="#0a78c8" stroke-width="2.2"><path d="M20 13v7H4V4h7"/><path d="M18 3l3 3-9 9H9v-3z"/></svg>
    <svg class="trash" width="16" height="19" viewBox="0 0 20 24" fill="#f05a5a"><path d="M1 4h18v2H1zM7 1h6v3H7zM3 7h14l-1 16H4zM7 9v12h1.5V9zM11.5 9v12H13V9z" fill-rule="evenodd"/></svg>
  </div>
  <div class="row" style="top:197px">
    <span class="name">Nursing</span><span class="sup">Lena Farrow</span>
    <span class="desc">Lorem Ipsum is simply dummy<br>printing and typesetting...</span>
    <span class="count">0</span><span class="badge">ACTIVE</span>
    <svg class="edit" width="18" height="18" viewBox="0 0 24 24" fill="none" stroke="#0a78c8" stroke-width="2.2"><path d="M20 13v7H4V4h7"/><path d="M18 3l3 3-9 9H9v-3z"/></svg>
    <svg class="trash" width="16" height="19" viewBox="0 0 20 24" fill="#f05a5a"><path d="M1 4h18v2H1zM7 1h6v3H7zM3 7h14l-1 16H4zM7 9v12h1.5V9zM11.5 9v12H13V9z" fill-rule="evenodd"/></svg>
  </div>
  <div class="row alt" style="top:277px">
    <span class="name">Nursing</span><span class="sup">Lena Farrow</span>
    <span class="desc">Lorem Ipsum is simply dummy<br>printing and typesetting...</span>
    <span class="count">0</span><span class="badge">ACTIVE</span>
    <svg class="edit" width="18" height="18" viewBox="0 0 24 24" fill="none" stroke="#0a78c8" stroke-width="2.2"><path d="M20 13v7H4V4h7"/><path d="M18 3l3 3-9 9H9v-3z"/></svg>
    <svg class="trash" width="16" height="19" viewBox="0 0 20 24" fill="#f05a5a"><path d="M1 4h18v2H1zM7 1h6v3H7zM3 7h14l-1 16H4zM7 9v12h1.5V9zM11.5 9v12H13V9z" fill-rule="evenodd"/></svg>
  </div>
  <div class="row" style="top:349px">
    <span class="name">Nursing</span><span class="sup">Lena Farrow</span>
    <span class="desc">Lorem Ipsum is simply dummy<br>printing and typesetting...</span>
    <span class="count">0</span><span class="badge">ACTIVE</span>
    <svg class="edit" width="18" height="18" viewBox="0 0 24 24" fill="none" stroke="#0a78c8" stroke-width="2.2"><path d="M20 13v7H4V4h7"/><path d="M18 3l3 3-9 9H9v-3z"/></svg>
    <svg class="trash" width="16" height="19" viewBox="0 0 20 24" fill="#f05a5a"><path d="M1 4h18v2H1zM7 1h6v3H7zM3 7h14l-1 16H4zM7 9v12h1.5V9zM11.5 9v12H13V9z" fill-rule="evenodd"/></svg>
  </div>
</section>

<div class="scrollbar"></div>

<p class="summary">Showing 1 to 12 of 15 entries</p>
<div class="pager-btn prev"><svg width="7" height="10" viewBox="0 0 7 10" fill="none" stroke="#6b7280" stroke-width="1.6"><path d="M6 1L2 5l4 4"/></svg>Prev</div>
<span class="page-num" style="left:928px">1</span>
<span class="page-current">2</span>
<span class="page-num" style="left:994px">3</span>
<span class="page-num" style="left:1019px">...</span>
<span class="page-num" style="left:1041px">82</span>
<div class="pager-btn next">Next<svg width="7" height="10" viewBox="0 0 7 10" fill="none" stroke="#fff" stroke-width="1.6"><path d="M1 1l4 4-4 4"/></svg></div>
</body>
</html>
```